FC Morlan - Creation of a AD banner for our yearly event

We are a local soccer club in Switzerland. We're organizing a event that will substitute to our yearly club dinner. We need a banner AD to promote on the social networks this event.
We would like to see design that use one or the 2 colors of the club (blue and red).
This Ad should link to a online shop where we can buy vouchers.

Requirements
Must have
• Logo of the club
Title : Fête des lanternes d'hiver
Call to action : Plus d'informations
Side texte : Grande Tombola
Banner size : W300xH250 or W300xH600
Nice to have
• Promotion texte: Soutenez le FC Morlan et les restaurateurs locaux

```html
<!DOCTYPE html>
<html lang="fr">
<head>
<meta charset="utf-8">
<title>FC Morlan – Fête des lanternes d'hiver</title>
<link href="https://fonts.googleapis.com/css2?family=Oswald:wght@500;600;700&display=swap" rel="stylesheet">
<style>
  :root {
    --club-red: #e4283c;
    --club-blue: #1b8ed6;
    --ink: #1d1d1f;
    --white: #ffffff;
    --photo-dark: #2a2224;
    --photo-red: #a3202f;
    --photo-green: #4f6a3c;
  }
  * { margin: 0; padding: 0; box-sizing: border-box; }
  html, body { width: 1200px; height: 2400px; overflow: hidden; background: var(--white); }
  .banner {
    position: relative;
    width: 1200px;
    height: 2400px;
    overflow: hidden;
    font-family: "Oswald", "Arial Narrow", sans-serif;
    background: var(--white);
  }
  .header {
    position: absolute;
    inset: 0 0 auto 0;
    height: 352px;
    background: var(--white);
    display: flex;
    align-items: center;
    padding-left: 48px;
    z-index: 3;
  }
  .club-mark {
    width: 200px;
    height: 200px;
    background: var(--club-red);
    margin-right: 76px;
  }
  .club-name {
    font-weight: 700;
    font-size: 124px;
    line-height: 1;
    color: var(--ink);
    letter-spacing: 1px;
    text-transform: uppercase;
  }
  .stage {
    position: absolute;
    top: 352px;
    left: 0;
    width: 1200px;
    height: 2048px;
    overflow: hidden;
  }
  .stage-photo {
    position: absolute;
    inset: 0;
    background:
      radial-gradient(ellipse 520px 900px at 720px 1000px, var(--photo-red), transparent 70%),
      radial-gradient(ellipse 380px 700px at 180px 900px, #8e1e2b, transparent 70%),
      linear-gradient(180deg, var(--photo-dark) 0%, #3a2f2c 45%, var(--photo-green) 82%, #3b5230 100%);
  }
  .stage-shade {
    position: absolute;
    inset: 0;
    background: linear-gradient(180deg, rgba(0,0,0,0) 30%, rgba(0,0,0,0.25) 50%, rgba(0,0,0,0) 70%);
  }
  .ribbon {
    position: absolute;
    left: 1020px;
    top: 260px;
    width: 1000px;
    height: 116px;
    margin-left: -500px;
    margin-top: -58px;
    transform: rotate(45deg);
    background: var(--club-red);
    border-top: 6px solid var(--white);
    border-bottom: 6px solid var(--white);
    display: flex;
    align-items: center;
    justify-content: center;
    color: var(--white);
    font-weight: 700;
    font-size: 60px;
    letter-spacing: 1px;
    text-transform: uppercase;
    z-index: 2;
  }
  .title {
    position: absolute;
    top: 1200px;
    left: 0;
    width: 1200px;
    text-align: center;
    color: var(--white);
    font-weight: 600;
    font-size: 116px;
    line-height: 1.3;
    text-shadow: 0 4px 18px rgba(0,0,0,0.45);
    z-index: 2;
  }
  .title .accent { color: var(--club-red); }
  .cta {
    position: absolute;
    left: 220px;
    top: 2092px;
    width: 760px;
    height: 240px;
    background: var(--club-blue);
    border: 8px solid var(--white);
    border-radius: 18px;
    color: var(--white);
    font-weight: 500;
    font-size: 66px;
    display: flex;
    align-items: center;
    justify-content: center;
    text-decoration: none;
    z-index: 3;
  }
</style>
</head>
<body>
<div class="banner">
  <header class="header">
    <div class="club-mark"></div>
    <div class="club-name">FC Morlan</div>
  </header>

  <section class="stage">
    <div class="stage-photo" role="img" aria-label="Joueurs du club en maillot rouge en action sur le terrain, ballon au pied"></div>
    <div class="stage-shade"></div>
    <div class="ribbon">Grande tombola</div>
  </section>

  <h1 class="title">Fête des <span class="accent">lanternes</span><br>d'hiver</h1>

  <a class="cta" href="#">Plus d'informations</a>
</div>
</body>
</html>
```